Pantry Barn EPP Mailer

This card will be mailed to local communities to make people aware of the ALL the Products - particularly local food - offered at Pantry Barn of Willowbrook. On the attached copy, the content in BOLD should be emphasized. Not all of the photos need to be utilized, but wanted to provide an assortment that shows off food and merchandise. Please note - this card is 8 in. x 6.5 inches and MUST be laid out to conform the the Each Porch Post format attached - with mailing and postage spaces left in the areas indicated on one side.

```html
<!DOCTYPE html>
<html lang="en">
<head>
<meta charset="utf-8">
<title>Pantry Barn EPP Mailer</title>
<link rel="stylesheet" href="https://fonts.googleapis.com/css2?family=Lobster&family=Open+Sans:wght@400;600;700&display=swap">
<style>
  :root {
    --leaf: #528d32;
    --leaf-dark: #3f7325;
    --cream: #f7f4c9;
    --wood: #6e4b30;
    --wood-dark: #4b3220;
    --paper: #ffffff;
    --ink-soft: #6a5a45;
    --backdrop: #e9e7e2;
  }
  * { box-sizing: border-box; margin: 0; padding: 0; }
  html, body { width: 1200px; height: 900px; overflow: hidden; }
  body {
    background: var(--backdrop);
    font-family: "Open Sans", Arial, sans-serif;
    position: relative;
  }
  .postcard {
    position: absolute;
    top: 222px;
    width: 560px;
    height: 455px;
    overflow: hidden;
    background: var(--paper);
    box-shadow: 0 6px 18px rgba(0,0,0,.18);
  }
  .postcard--front { left: 30px; }
  .postcard--back { left: 610px; }
  .postcard__art { position: absolute; inset: 0; width: 560px; height: 455px; display: block; }
  .abs { position: absolute; }

  /* front */
  .store-name { color: var(--paper); font-weight: 400; line-height: 1.05; }
  .store-name__main { font-size: 34px; display: block; }
  .store-name__place { font-size: 25px; display: block; }
  .feature-pill {
    background: var(--cream); color: var(--leaf-dark);
    font-weight: 700; font-size: 13px; letter-spacing: .3px;
    padding: 4px 22px 4px 14px; border-radius: 14px;
  }
  .feature-list { list-style: none; color: var(--paper); font-size: 16px; }
  .feature-list li { display: flex; align-items: center; gap: 9px; height: 24px; }
  .feature-list .dot {
    width: 18px; height: 18px; border-radius: 50%;
    border: 1.5px solid var(--cream); background: rgba(255,255,255,.12);
    flex: none;
  }
  .script { font-family: "Lobster", cursive; }
  .open-days { color: var(--cream); font-size: 24px; line-height: 30px; }
  .perks { list-style: none; color: var(--paper); font-size: 11px; font-weight: 600; line-height: 14px; }
  .perks li { display: flex; align-items: center; gap: 5px; }
  .address { color: var(--paper); font-size: 12px; font-weight: 600; line-height: 16px; font-style: normal; }
  .rule { width: 1px; height: 46px; background: rgba(247,244,201,.6); }
  .badge-text {
    color: var(--leaf-dark); font-size: 14px; line-height: 16px; text-align: center;
  }

  /* back */
  .discover { color: var(--cream); font-size: 21px; line-height: 24px; font-weight: 400; }
  .body-copy { color: var(--paper); font-size: 11px; line-height: 14px; width: 260px; }
  .body-copy p + p { margin-top: 6px; }
  .open-pill {
    background: var(--cream); color: var(--leaf-dark);
    font-size: 16px; line-height: 20px; padding: 2px 18px; border-radius: 13px;
  }
  .contact { color: var(--paper); font-size: 11px; font-weight: 700; display: flex; align-items: center; gap: 5px; line-height: 16px; }
  .contact--phone {
    background: var(--leaf); padding: 2px 10px 2px 4px; border-radius: 12px; font-size: 14px; line-height: 18px;
  }
  .contact .icon { width: 16px; height: 16px; flex: none; }
  .return-name { color: var(--leaf); font-size: 17px; font-weight: 400; line-height: 1.1; }
  .return-address { color: var(--ink-soft); font-size: 9.5px; font-weight: 600; line-height: 12px; margin-top: 6px; }
  .stamp-box { width: 66px; height: 74px; border: 1px solid #777; }
</style>
</head>
<body>

<!-- Front side -->
<section class="postcard postcard--front">
  <svg class="postcard__art" viewBox="0 0 560 455" xmlns="http://www.w3.org/2000/svg">
    <defs>
      <linearGradient id="shelfTone" x1="0" y1="0" x2="1" y2="0">
        <stop offset="0" stop-color="#d9c36a"/>
        <stop offset=".5" stop-color="#a8865a"/>
        <stop offset="1" stop-color="#8a6b4a"/>
      </linearGradient>
      <linearGradient id="woodTone" x1="0" y1="0" x2="0" y2="1">
        <stop offset="0" stop-color="#7a5337"/>
        <stop offset="1" stop-color="#4b3220"/>
      </linearGradient>
      <linearGradient id="greenTone" x1="0" y1="0" x2="0" y2="1">
        <stop offset="0" stop-color="#5b9838"/>
        <stop offset="1" stop-color="#467d29"/>
      </linearGradient>
      <radialGradient id="tomatoTone"><stop offset="0" stop-color="#e58a3a"/><stop offset="1" stop-color="#9a4a2c"/></radialGradient>
      <radialGradient id="jarTone"><stop offset="0" stop-color="#c9a15d"/><stop offset="1" stop-color="#5a3f2b"/></radialGradient>
      <radialGradient id="cheeseTone"><stop offset="0" stop-color="#f2e49a"/><stop offset="1" stop-color="#b9a36a"/></radialGradient>
      <radialGradient id="breadTone"><stop offset="0" stop-color="#c49b6a"/><stop offset="1" stop-color="#6d4f36"/></radialGradient>
      <radialGradient id="vegTone"><stop offset="0" stop-color="#d24a2c"/><stop offset=".55" stop-color="#5f8f2e"/><stop offset="1" stop-color="#6e4b30"/></radialGradient>
    </defs>

    <g role="img" aria-label="Photo of shelf with bags of local flour and polenta">
      <rect x="0" y="0" width="560" height="128" fill="url(#shelfTone)"/>
    </g>
    <rect x="0" y="128" width="560" height="238" fill="url(#greenTone)"/>
    <rect x="0" y="366" width="560" height="89" fill="url(#woodTone)"/>
    <line x1="0" y1="128" x2="560" y2="128" stroke="var(--cream)" stroke-width="3"/>
    <line x1="0" y1="366" x2="560" y2="366" stroke="var(--cream)" stroke-width="3"/>

    <g role="img" aria-label="Photo of organic heirloom tomatoes in a wooden crate">
      <circle cx="485" cy="55" r="92" fill="url(#tomatoTone)" stroke="var(--cream)" stroke-width="3"/>
    </g>
    <g role="img" aria-label="Photo of shelves with international sauces and bottles">
      <circle cx="360" cy="160" r="62" fill="url(#jarTone)" stroke="var(--cream)" stroke-width="3"/>
    </g>
    <g role="img" aria-label="Photo of wedges of local cheese">
      <circle cx="505" cy="195" r="70" fill="url(#cheeseTone)" stroke="var(--cream)" stroke-width="3"/>
    </g>
    <g role="img" aria-label="Photo of fresh baked breads">
      <circle cx="440" cy="285" r="60" fill="url(#breadTone)" stroke="var(--cream)" stroke-width="3"/>
    </g>
    <g role="img" aria-label="Photo of a basket spilling fresh peppers, beans and vegetables">
      <path d="M400 455 Q405 335 500 305 Q545 297 560 305 L560 455 Z" fill="url(#vegTone)"/>
    </g>

    <circle cx="345" cy="262" r="44" fill="var(--cream)" stroke="#e7e2a8" stroke-width="4" stroke-dasharray="3 3"/>
  </svg>

  <h1 class="store-name abs" style="left:22px; top:140px;">
    <span class="store-name__main">Pantry Barn</span>
    <span class="store-name__place">of Willowbrook</span>
  </h1>

  <div class="feature-pill abs" style="left:22px; top:220px;">PROUDLY FEATURES:</div>

  <ul class="feature-list abs" style="left:26px; top:248px;">
    <li><span class="dot"></span>Local Produce, Meat &amp; Cheese</li>
    <li><span class="dot"></span>Local Breads &amp; Sweets</li>
    <li><span class="dot"></span>International Foods</li>
    <li><span class="dot"></span>Kitchen • Home • Gift Items</li>
  </ul>

  <div class="badge-text script abs" style="left:301px; top:238px; width:88px;">Make A Day<br>of It in<br>Willowbrook!</div>

  <div class="open-days script abs" style="left:22px; top:368px;">Open 7 Days!</div>
  <ul class="perks abs" style="left:24px; top:401px;">
    <li><svg width="10" height="10" viewBox="0 0 10 10"><circle cx="5" cy="5" r="4.3" fill="none" stroke="var(--cream)"/><path d="M2.8 5.2 L4.4 6.7 L7.3 3.5" fill="none" stroke="var(--cream)" stroke-width="1.3"/></svg>Family-Run</li>
    <li><svg width="10" height="10" viewBox="0 0 10 10"><circle cx="5" cy="5" r="4.3" fill="none" stroke="var(--cream)"/><path d="M2.8 5.2 L4.4 6.7 L7.3 3.5" fill="none" stroke="var(--cream)" stroke-width="1.3"/></svg>Locally Focused</li>
    <li><svg width="10" height="10" viewBox="0 0 10 10"><circle cx="5" cy="5" r="4.3" fill="none" stroke="var(--cream)"/><path d="M2.8 5.2 L4.4 6.7 L7.3 3.5" fill="none" stroke="var(--cream)" stroke-width="1.3"/></svg>Kind Service</li>
  </ul>
  <div class="rule abs" style="left:172px; top:380px;"></div>
  <address class="address abs" style="left:184px; top:376px;">
    Corner of Orchard &amp; Mill Streets<br>
    212 Orchard Lane, Willowbrook<br>
    555 014-2290
  </address>
</section>

<!-- Back side -->
<section class="postcard postcard--back">
  <svg class="postcard__art" viewBox="0 0 560 455" xmlns="http://www.w3.org/2000/svg">
    <defs>
      <linearGradient id="breadShelfTone" x1="0" y1="0" x2="1" y2="1">
        <stop offset="0" stop-color="#c7a680"/>
        <stop offset="1" stop-color="#6f5a48"/>
      </linearGradient>
      <linearGradient id="woodToneB" x1="0" y1="0" x2="0" y2="1">
        <stop offset="0" stop-color="#7a5337"/>
        <stop offset="1" stop-color="#4b3220"/>
      </linearGradient>
      <linearGradient id="greenToneB" x1="0" y1="0" x2="0" y2="1">
        <stop offset="0" stop-color="#5b9838"/>
        <stop offset="1" stop-color="#467d29"/>
      </linearGradient>
      <radialGradient id="caseTone"><stop offset="0" stop-color="#d9c9a8"/><stop offset="1" stop-color="#6b6a5c"/></radialGradient>
      <radialGradient id="peachTone"><stop offset="0" stop-color="#f0a24a"/><stop offset="1" stop-color="#b13a2a"/></radialGradient>
      <radialGradient id="giftTone"><stop offset="0" stop-color="#8fc6d6"/><stop offset="1" stop-color="#3f7f95"/></radialGradient>
    </defs>

    <g role="img" aria-label="Photo of a bakery case with wrapped loaves of bread">
      <rect x="0" y="0" width="400" height="150" fill="url(#breadShelfTone)"/>
    </g>
    <rect x="0" y="150" width="400" height="216" fill="url(#greenToneB)"/>
    <rect x="0" y="366" width="420" height="89" fill="url(#woodToneB)"/>
    <line x1="0" y1="150" x2="400" y2="150" stroke="var(--cream)" stroke-width="3"/>
    <line x1="0" y1="366" x2="420" y2="366" stroke="var(--cream)" stroke-width="3"/>

    <path d="M345 0 Q250 230 410 455 L560 455 L560 0 Z" fill="var(--paper)"/>
    <path d="M345 0 Q250 230 410 455" fill="none" stroke="var(--cream)" stroke-width="4"/>

    <g role="img" aria-label="Photo of a deli case with prepared foods">
      <circle cx="62" cy="366" r="38" fill="url(#caseTone)" stroke="var(--cream)" stroke-width="3"/>
    </g>
    <g role="img" aria-label="Photo of a bowl of ripe peaches">
      <circle cx="146" cy="360" r="38" fill="url(#peachTone)" stroke="var(--cream)" stroke-width="3"/>
    </g>
    <g role="img" aria-label="Photo of home and gift items on shelves">
      <circle cx="230" cy="354" r="38" fill="url(#giftTone)" stroke="var(--cream)" stroke-width="3"/>
    </g>

    <circle cx="290" cy="172" r="42" fill="var(--cream)" stroke="#e7e2a8" stroke-width="4" stroke-dasharray="3 3"/>
  </svg>

  <div class="badge-text script abs" style="left:246px; top:150px; width:88px; font-size:13px; line-height:15px;">Make A Day<br>of It in<br>Willowbrook!</div>

  <h2 class="discover script abs" style="left:20px; top:162px;">Discover our many<br>Regional Food Items</h2>

  <div class="body-copy abs" style="left:20px; top:214px;">
    <p>Choosing locally grown/produced, healthy food benefits you, your neighbors &amp; our planet. We like that.</p>
    <p>Please stop in and see the changes we have in store…with more to come!</p>
  </div>

  <div class="open-pill script abs" style="left:96px; top:292px;">Open 7 Days!</div>

  <div class="contact contact--phone abs" style="left:112px; top:407px;">
    <svg class="icon" viewBox="0 0 16 16"><circle cx="8" cy="8" r="8" fill="var(--paper)"/><path d="M5.2 4 L6.8 4 L7.3 6 L6.3 6.8 Q7.2 8.8 9.2 9.7 L10 8.7 L12 9.2 L12 10.8 Q8 11.5 5 7.8 Q4.4 6 5.2 4 Z" fill="var(--leaf)"/></svg>
    555 014-2290
  </div>
  <div class="contact abs" style="left:20px; top:434px;">
    <svg class="icon" viewBox="0 0 16 16"><circle cx="8" cy="8" r="7" fill="var(--leaf)" stroke="var(--paper)"/><ellipse cx="8" cy="8" rx="3" ry="7" fill="none" stroke="var(--paper)"/><line x1="1" y1="8" x2="15" y2="8" stroke="var(--paper)"/></svg>
    PBOW.net
  </div>
  <div class="contact abs" style="left:220px; top:434px;">
    <svg class="icon" viewBox="0 0 16 16"><circle cx="8" cy="8" r="8" fill="var(--leaf)"/><rect x="4" y="5.5" width="8" height="5.5" fill="none" stroke="var(--paper)"/><path d="M4 5.5 L8 8.5 L12 5.5" fill="none" stroke="var(--paper)"/></svg>
    hello@pantrybarn.net
  </div>

  <div class="abs" style="left:330px; top:60px;">
    <div class="return-name">Pantry Barn<br>of Willowbrook</div>
    <div class="return-address">Corner of Orchard &amp; Mill Streets<br>212 Orchard Lane, Willowbrook</div>
  </div>

  <div class="stamp-box abs" style="right:20px; top:18px;"></div>
</section>

</body>
</html>
```